Create a business card with the logo

The business card needs to have a general theme for 3 doctors' names to be used, and of course, one doctor's name at a time per card. I'd like a design that plays off of our logo. Something fun and cool, not childish. The back side will have a QR code that leads to our website, which is still to be developed. Logo file is attached.

```html
<!DOCTYPE html>
<html lang="en">
<head>
<meta charset="utf-8">
<title>Larkfield Pediatric Dentistry – Business Card</title>
<link rel="stylesheet" href="https://fonts.googleapis.com/css2?family=Poppins:wght@300;400;600;700&display=swap">
<style>
  :root {
    --bg: #222222;
    --card-dark: #1d1d1d;
    --teal: #35bac6;
    --teal-deep: #12a2aa;
    --orange: #f26b24;
    --white: #ffffff;
  }
  * { margin: 0; padding: 0; box-sizing: border-box; }
  html, body { width: 1200px; height: 780px; overflow: hidden; background: var(--bg); }
  body { font-family: "Poppins", sans-serif; position: relative; }

  .card {
    position: absolute;
    top: 230px;
    width: 560px;
    height: 320px;
    overflow: hidden;
    box-shadow: 0 18px 40px rgba(0,0,0,0.55);
  }
  .card-front { left: 30px; background: var(--card-dark); }
  .card-back { left: 610px; background: var(--teal); }

  .front-art { position: absolute; inset: 0; }

  .brand { position: absolute; display: flex; align-items: flex-end; gap: 10px; }
  .brand-name { font-weight: 600; line-height: 1; letter-spacing: -1px; }
  .brand-tagline { font-weight: 600; text-transform: uppercase; line-height: 1.15; letter-spacing: 1.2px; padding-bottom: 4px; }

  .card-front .brand { top: 28px; left: 130px; }
  .card-front .brand-name { font-size: 54px; color: var(--teal); }
  .card-front .brand-tagline { font-size: 10px; color: var(--orange); }

  .person { position: absolute; top: 150px; left: 38px; }
  .person-name { font-size: 32px; line-height: 1.1; }
  .person-first { font-weight: 700; color: var(--orange); }
  .person-last { font-weight: 300; color: var(--teal); }
  .person-role { font-size: 15px; color: var(--white); margin-top: 4px; padding-left: 70px; }

  .divider { position: absolute; left: 290px; top: 140px; width: 2px; height: 66px; background: var(--teal); }

  .contacts { position: absolute; top: 92px; left: 310px; list-style: none; }
  .contact { display: flex; align-items: center; gap: 10px; font-size: 14px; color: var(--white); height: 24px; }
  .contact-icon { width: 15px; height: 15px; flex: none; }

  .address { font-size: 13px; fill: var(--white); font-family: "Poppins", sans-serif; }

  .card-back .brand { top: 112px; left: 0; right: 0; justify-content: center; }
  .card-back .brand-name { font-size: 74px; color: var(--teal-deep); }
  .card-back .brand-tagline { font-size: 12px; color: var(--teal-deep); padding-bottom: 8px; }
</style>
</head>
<body>

<section class="card card-front" aria-label="Business card front">
  <svg class="front-art" viewBox="0 0 560 320" width="560" height="320" aria-hidden="true">
    <defs>
      <path id="address-line" d="M255,318 C390,298 510,240 558,180"/>
    </defs>
    <path class="swoosh-band" d="M160,320 C350,295 500,235 560,150 L560,320 Z" fill="var(--orange)"/>
    <path class="swoosh-line" d="M110,320 C320,290 500,230 556,140" fill="none" stroke="var(--teal)" stroke-width="3"/>
    <text class="address"><textPath href="#address-line">480 Maple Crest Rd. Suite 12 Cedar Falls, TX 75310</textPath></text>
  </svg>

  <div class="brand">
    <span class="brand-name">larkfield</span>
    <span class="brand-tagline">Pediatric Dentistry<br>and Orthodontics</span>
  </div>

  <div class="person">
    <p class="person-name"><span class="person-first">Maren</span> <span class="person-last">Holt</span></p>
    <p class="person-role">Founder &amp; CEO</p>
  </div>

  <div class="divider"></div>

  <ul class="contacts">
    <li class="contact">
      <svg class="contact-icon" viewBox="0 0 16 16"><path d="M4 1.5 L6.5 4.5 L5 6 C6 8.2 7.8 10 10 11 L11.5 9.5 L14.5 12 L12.5 14.5 C7 14 2 9 1.5 3.5 Z" fill="var(--orange)"/></svg>
      (555) 014-2231
    </li>
    <li class="contact">
      <svg class="contact-icon" viewBox="0 0 16 16"><circle cx="8" cy="8" r="7" fill="var(--orange)"/><path d="M1 8 H15 M8 1 C4.5 4.5 4.5 11.5 8 15 M8 1 C11.5 4.5 11.5 11.5 8 15" stroke="var(--card-dark)" stroke-width="1" fill="none"/></svg>
      info@larkfieldsmiles.com
    </li>
    <li class="contact">
      <svg class="contact-icon" viewBox="0 0 16 16"><rect x="1" y="3" width="14" height="10" rx="1.5" fill="var(--orange)"/><path d="M1.5 3.8 L8 9 L14.5 3.8" stroke="var(--card-dark)" stroke-width="1.2" fill="none"/></svg>
      www.larkfieldsmiles.com
    </li>
  </ul>
</section>

<section class="card card-back" aria-label="Business card back">
  <div class="brand">
    <span class="brand-name">larkfield</span>
    <span class="brand-tagline">Pediatric Dentistry<br>and Orthodontics</span>
  </div>
</section>

</body>
</html>
```